Re-design my 1-page website to be BETTER!

Hi Guys,
I recently created a 1-page website for market testing purposes for a company I am starting. Problem is, the feedback i've had on the page is its a bit corporate and boring.
I would love you to design something that is fresher, more modern and will generate leads (via the sign up CTA's).
Here is the website as it is now: www.guidelinkhub.com.au.
If you need any info or have questions, just reach out.
Thanks,
Oliver

Target Market(s)

Entrepreneurs

Number of Pages Required

1 page

Font styles to use
Sans Serif

Colors
abd036
34a6d7
ffffff

Requirements
Must have
• Fresh, Modern, high-converting
• I expect 70% of traffic to be mobile so must be mobile optimised first.
Nice to have
• I've highlighted colours i like below, however, I am open to suggestions. I like colours that are gender neutral and show energy and vibrancy.
• I have used Proxima Nova for the fonts, as I find it easy to read however, I am open to suggestions. My main preference is that it displays well and is easily read

```html
<!DOCTYPE html>
<html lang="en">
<head>
<meta charset="utf-8">
<title>GuideLink Hub – A Mentor For Everyone</title>
<link href="https://fonts.googleapis.com/css2?family=Open+Sans:wght@300;400;600;700&display=swap" rel="stylesheet">
<style>
:root{
  --green:#67cf2c;
  --green-soft:#abd036;
  --teal:#2fa7a4;
  --blue:#34a6d7;
  --ink:#4d4d4d;
  --muted:#8a8a8a;
  --line:#e3e3e3;
  --grey-bg:#f3f3f3;
  --white:#ffffff;
  --dark:#3a4144;
}
*{box-sizing:border-box;margin:0;padding:0}
html,body{width:1200px;height:4336px;overflow:hidden}
body{font-family:"Open Sans",Arial,sans-serif;color:var(--ink);background:var(--white)}
.section{position:relative;width:1200px;overflow:hidden}
.btn{display:inline-block;background:var(--green);color:var(--white);font-size:14px;font-weight:700;letter-spacing:2px;text-transform:uppercase;padding:16px 40px;border-radius:30px}
.btn-outline{background:rgba(255,255,255,.12);border:2px solid var(--green)}
.center{text-align:center}
.h2{font-size:40px;font-weight:400;color:var(--ink);line-height:1.25}
.small-note{font-size:14px;color:var(--ink);margin-top:18px;line-height:1.5}

/* hero */
.hero{height:600px}
.hero-photo{position:absolute;inset:0;background:linear-gradient(120deg,#3fb6a7 0%,#2c9c9c 45%,#1f7e86 100%)}
.hero-photo::after{content:"";position:absolute;inset:0;background:radial-gradient(circle at 20% 40%,rgba(255,255,255,.18),transparent 40%),radial-gradient(circle at 85% 30%,rgba(0,0,0,.15),transparent 45%)}
.hero-inner{position:relative;text-align:center;color:var(--white);padding-top:58px}
.brand{font-size:26px;font-weight:700;letter-spacing:1px}
.brand-tag{font-size:16px;font-weight:600;margin-top:4px}
.hero-quote{font-size:30px;font-weight:300;font-style:italic;line-height:1.4;width:820px;margin:70px auto 0}
.hero-sub{font-size:12px;letter-spacing:3px;margin-top:28px;opacity:.85;text-transform:uppercase}
.hero .btn{margin-top:40px}

/* intro */
.intro{height:550px;display:flex}
.intro-text{width:600px;padding:60px 50px 0 160px}
.intro-text h2{font-size:40px;font-weight:400;line-height:1.2;color:var(--ink)}
.intro-text p{font-size:13px;line-height:1.7;color:var(--muted);margin-top:18px}
.intro-text .btn{margin-top:30px;padding:14px 34px}
.intro-photo{width:600px;height:550px;background:linear-gradient(135deg,#d9dcde 0%,#b7b2ab 40%,#8c6b5a 70%,#5c4a44 100%)}

/* steps */
.steps{height:860px;background:var(--grey-bg);padding-top:90px}
.steps .h2 span{color:var(--blue)}
.steps .lead{font-size:13px;color:var(--muted);line-height:1.6;width:560px;margin:20px auto 0}
.steps .lead b{color:var(--ink)}
.cards{display:flex;justify-content:center;gap:22px;margin-top:50px}
.card{width:278px;height:314px;background:var(--white);padding:36px 30px;text-align:center;box-shadow:0 2px 8px rgba(0,0,0,.05)}
.card.raised{box-shadow:0 10px 30px rgba(0,0,0,.14);transform:translateY(-8px)}
.card h3{font-size:14px;font-weight:600;color:var(--green);margin-top:24px}
.card p{font-size:12px;line-height:1.7;color:var(--muted);margin-top:14px}
.steps .btn{margin-top:104px}

/* benefits */
.benefits{height:870px;padding-top:60px}
.benefits .h2{width:520px;margin:0 auto}
.grid{display:grid;grid-template-columns:repeat(3,280px);column-gap:40px;row-gap:44px;justify-content:center;margin-top:70px}
.benefit h3{font-size:15px;font-weight:600;color:var(--green);text-align:center}
.benefit p{font-size:12px;line-height:1.7;color:var(--muted);margin-top:16px;text-align:center}
.benefits .btn{margin-top:70px}

/* faq */
.faq{height:1000px;background:var(--grey-bg);padding-top:255px}
.faq-list{width:760px;margin:50px auto 0}
.faq-item{display:flex;justify-content:space-between;align-items:center;border-bottom:1px solid var(--line);height:58px;font-size:16px;color:var(--green);font-weight:600}
.faq-open{background:var(--white);border:1px solid var(--line);padding:22px 26px;margin-bottom:10px}
.faq-open .q{display:flex;justify-content:space-between;font-size:16px;color:var(--green);font-weight:600;padding-bottom:18px;border-bottom:1px solid var(--line)}
.faq-open p{font-size:12px;line-height:1.7;color:var(--muted);margin-top:12px}

/* closing */
.closing{height:456px}
.closing-photo{position:absolute;inset:0;background:linear-gradient(180deg,#6d7376 0%,#4e5558 60%,#3a4144 100%)}
.closing-inner{position:relative;text-align:center;color:var(--white);padding-top:60px}
.closing-inner h2{font-size:40px;font-weight:400}
.closing-inner h2 span{color:var(--green)}
.closing-inner p{font-size:14px;line-height:1.7;width:620px;margin:18px auto 0;opacity:.9}
.closing .btn{margin-top:26px}
</style>
</head>
<body>

<section class="section hero">
  <div class="hero-photo" role="img" aria-label="Teal-tinted photo of a mentoring meeting around an office table"></div>
  <div class="hero-inner">
    <div class="brand">GuideLink Hub</div>
    <div class="brand-tag">A Mentor For Everyone</div>
    <p class="hero-quote">“We’ve flipped the model on its head - so now you choose your Mentor. It’s never been this easy to get the advice and guidance you need to thrive”</p>
    <p class="hero-sub">Advice · Guidance · Support</p>
    <a class="btn btn-outline">Find My Mentor &#9656;</a>
  </div>
</section>

<section class="section intro">
  <div class="intro-text">
    <h2>Finding a Mentor Has Never Been Easier</h2>
    <p>Having a great mentor can truly change your business, professional or personal growth. But unless you know an incredible network, finding great mentors has always been a challenge.</p>
    <p>GuideLink Hub is changing that by putting the choice back into your hands, giving you access to a trusted community of experienced Mentors ready to help you move forward.</p>
    <p>We begin with you and end by connecting you to your Mentor, matching the perfect balance of experience, skills and personality to guide you toward your goals.</p>
    <a class="btn">Let’s Get Started</a>
  </div>
  <div class="intro-photo" role="img" aria-label="Photo of a smiling professional woman in glasses"></div>
</section>

<section class="section steps center">
  <h2 class="h2">Mentorship: <span>But Different</span></h2>
  <p class="lead">Finding the perfect mentor has never been simpler. We've made mentorship accessible to everyone – because <b>Mentors seek you.</b></p>
  <div class="cards">
    <div class="card">
      <svg width="70" height="70" viewBox="0 0 70 70"><circle cx="35" cy="35" r="33" fill="none" stroke="#9a9a9a" stroke-width="1.5"/><text x="35" y="46" text-anchor="middle" font-family="Open Sans,sans-serif" font-size="30" font-weight="300" fill="#777">1</text></svg>
      <h3>Tell Us What Matters</h3>
      <p>Share a little about who you are, where you want to go and the challenges you are facing right now so we can find the best fit.</p>
    </div>
    <div class="card raised">
      <svg width="70" height="70" viewBox="0 0 70 70"><circle cx="35" cy="35" r="33" fill="none" stroke="#9a9a9a" stroke-width="1.5"/><text x="35" y="46" text-anchor="middle" font-family="Open Sans,sans-serif" font-size="30" font-weight="300" fill="#777">2</text></svg>
      <h3>Choose Your Mentor</h3>
      <p>Mentors are matched to you, then you choose the one you feel most comfortable with. No pressure, simply the right person.</p>
    </div>
    <div class="card">
      <svg width="70" height="70" viewBox="0 0 70 70"><circle cx="35" cy="35" r="33" fill="none" stroke="#9a9a9a" stroke-width="1.5"/><text x="35" y="46" text-anchor="middle" font-family="Open Sans,sans-serif" font-size="30" font-weight="300" fill="#777">3</text></svg>
      <h3>Ongoing Support</h3>
      <p>Meet regularly and keep your momentum, with your Mentor there to share insight whenever you need it most.</p>
    </div>
  </div>
  <a class="btn">Register For Free</a>
  <p class="small-note">100% confidential and 100% obligation free</p>
</section>

<section class="section benefits center">
  <h2 class="h2">How a Mentor Will Accelerate Your Growth</h2>
  <div class="grid">
    <div class="benefit"><h3>Tailored advice</h3><p>Insights based on real experience from someone who has faced the same challenges you are facing today and found a way through.</p></div>
    <div class="benefit"><h3>Avoid the Pitfalls</h3><p>An experienced Mentor will help you see the challenges before they arrive, saving you time, money and plenty of stress.</p></div>
    <div class="benefit"><h3>A Supportive Ear</h3><p>Running a business can be lonely. A Mentor is someone to talk through ideas with who wants to see you succeed.</p></div>
    <div class="benefit"><h3>Clarity</h3><p>Sometimes we are too close to see the big picture. A Mentor will help you cut through the noise and focus on what matters.</p></div>
    <div class="benefit"><h3>Motivation</h3><p>Your Mentor has been there before and knows how to keep you moving forward when the going gets tough.</p></div>
    <div class="benefit"><h3>Make you Accountable</h3><p>A Mentor will hold you to your word, checking in on your goals and making sure you follow through every time.</p></div>
  </div>
  <a class="btn">Register For Free</a>
  <p class="small-note">Your chance to find your perfect mentor from your home.<br>Register today to take the next step in your life.</p>
</section>

<section class="section faq">
  <h2 class="h2 center">Frequently Asked Questions</h2>
  <div class="faq-list">
    <div class="faq-open">
      <div class="q"><span>What is a Mentor?</span><span>&#8722;</span></div>
      <p>Experienced and Trusted Advisor – Guide – Confidante – Friend</p>
      <p>A mentor is someone with more experience who is willing to share knowledge and advice with a less experienced person, helping them grow with confidence.</p>
      <p>A good Mentor listens, challenges your thinking and helps you see opportunities you might have missed, all within a supportive and confidential relationship.</p>
      <p>Importantly, a great Mentor should be someone you feel comfortable with, and that is why we let you choose.</p>
    </div>
    <div class="faq-item"><span>Is a Mentor right for me?</span><span>+</span></div>
    <div class="faq-item"><span>How often do we meet?</span><span>+</span></div>
    <div class="faq-item"><span>Can I have more than one Mentor?</span><span>+</span></div>
    <div class="faq-item"><span>What if it doesn’t work out?</span><span>+</span></div>
    <div class="faq-item"><span>How do we meet?</span><span>+</span></div>
    <div class="faq-item"><span>What are the costs?</span><span>+</span></div>
  </div>
</section>

<section class="section closing">
  <div class="closing-photo" role="img" aria-label="Darkened photo of people networking at an event"></div>
  <div class="closing-inner">
    <h2>It’s Time to Invest in <span>You</span></h2>
    <p>If you are looking for the right person to guide your next step, register today and discover a Mentor who truly understands your journey.</p>
    <p>Find your Mentor in a few simple steps.</p>
    <p>Add your name to our community and start your journey now.</p>
    <a class="btn">Get On Trial</a>
    <p>Sign up today, completely free and confidential.</p>
  </div>
</section>

</body>
</html>
```